Lotus Leaf Kitchen Road Billboard

Road Billboard I need all of this information on it
Authentic Thai Food Bangkok Style
6.5 Miles on the right
4126 Maple Ridge Rd Otto NC
828-555-4172

```html
<!DOCTYPE html>
<html lang="en">
<head>
<meta charset="UTF-8">
<title>Lotus Leaf Kitchen Road Billboard</title>
<link href="https://fonts.googleapis.com/css2?family=Great+Vibes&family=Montserrat:ital,wght@0,400;0,500;0,700;1,400;1,600;1,700&display=swap" rel="stylesheet">
<style>
  :root {
    --page-bg: #1e2833;
    --board-black: #0c0c0d;
    --board-frame: #f2f2ef;
    --gold: #d9a62a;
    --gold-band: #e0ae2e;
    --white: #ffffff;
    --ink: #141414;
    --wok: #2a2a2c;
  }
  * { margin: 0; padding: 0; box-sizing: border-box; }
  html, body { width: 1200px; height: 1200px; overflow: hidden; }
  body { background: var(--page-bg); position: relative; font-family: "Montserrat", sans-serif; }

  .billboard {
    position: absolute; left: 40px; top: 388px;
    width: 1120px; height: 424px;
    background: var(--board-black);
    border: 5px solid var(--board-frame);
    overflow: hidden;
  }
  .food-photo {
    position: absolute; left: 420px; top: 0; width: 700px; height: 100%;
    background:
      radial-gradient(ellipse 30% 40% at 35% 30%, rgba(235,120,40,.85), transparent 70%),
      radial-gradient(ellipse 40% 25% at 55% 92%, rgba(240,130,30,.9), transparent 70%),
      radial-gradient(ellipse 45% 30% at 55% 55%, #4a4340, var(--wok) 60%, transparent 75%),
      linear-gradient(90deg, var(--board-black) 0%, #1b1a19 25%, #2b2b2b 100%);
  }

  .brand { position: absolute; left: 147px; top: 50px; width: 200px; text-align: center; }
  .brand-mark { width: 44px; height: 44px; border-radius: 50%; background: var(--gold); margin: 0 auto 18px; }
  .brand-name { color: var(--gold); font-size: 17px; font-weight: 500; white-space: nowrap; }

  .tagline-top, .tagline-main, .tagline-bottom { position: absolute; white-space: nowrap; line-height: 1; }
  .tagline-top {
    left: 140px; top: 186px;
    color: var(--white); font-style: italic; font-weight: 400; font-size: 31px;
  }
  .tagline-main {
    left: 60px; top: 224px;
    font-family: "Great Vibes", cursive; color: var(--gold); font-size: 92px;
  }
  .tagline-bottom {
    left: 142px; top: 322px;
    color: var(--white); font-style: italic; font-weight: 400; font-size: 31px;
  }

  .phone { position: absolute; left: 730px; top: 48px; display: flex; align-items: center; gap: 14px; }
  .phone-icon { width: 52px; height: 52px; }
  .phone-number { color: var(--white); font-weight: 700; font-size: 37px; letter-spacing: .5px; white-space: nowrap; }

  .address-band {
    position: absolute; left: 770px; top: 118px; width: 350px; height: 34px;
    background: var(--gold-band); color: var(--ink);
    font-style: italic; font-weight: 700; font-size: 21px;
    line-height: 34px; padding-left: 12px; white-space: nowrap;
  }

  .direction-arrow { position: absolute; left: 540px; top: 316px; width: 560px; height: 92px; }
  .direction-text {
    position: absolute; left: 680px; top: 345px; width: 360px;
    color: var(--ink); font-weight: 500; font-size: 25px; white-space: nowrap;
  }
</style>
</head>
<body>
  <div class="billboard">
    <div class="food-photo" role="img" aria-label="Photo of a wok over bright flames with shrimp, broccoli and noodles tossed in the air"></div>

    <div class="brand">
      <div class="brand-mark"></div>
      <div class="brand-name">Lotus Leaf Kitchen</div>
    </div>

    <span class="tagline-top">Authentic</span>
    <span class="tagline-main">Thai Food</span>
    <span class="tagline-bottom">Bangkok Style</span>

    <div class="phone">
      <svg class="phone-icon" viewBox="0 0 24 24" fill="none" stroke="#ffffff" stroke-width="1.6" stroke-linejoin="round">
        <path d="M6.6 2.5h3l1.5 4.2-2 1.5a11 11 0 0 0 6.7 6.7l1.5-2 4.2 1.5v3a2 2 0 0 1-2.2 2A17.5 17.5 0 0 1 4.5 4.7a2 2 0 0 1 2.1-2.2z"/>
      </svg>
      <span class="phone-number">828-555-4172</span>
    </div>

    <div class="address-band">4126 Maple Ridge Rd Otto NC</div>

    <svg class="direction-arrow" viewBox="0 0 560 92" preserveAspectRatio="none">
      <defs>
        <linearGradient id="arrowFade" x1="0" x2="1" y1="0" y2="0">
          <stop offset="0" stop-color="#ffffff" stop-opacity="0"/>
          <stop offset="0.3" stop-color="#ffffff" stop-opacity="0.9"/>
          <stop offset="1" stop-color="#ffffff"/>
        </linearGradient>
      </defs>
      <path d="M0 22 H470 V0 L560 46 L470 92 V70 H0 Z" fill="url(#arrowFade)"/>
    </svg>
    <div class="direction-text">6.5 Miles on the right</div>
  </div>
</body>
</html>
```